Nightclub promoter business cards

We need business cards designed for our company based in Toronto, Canada called "NowQuillo". We are an events company that promotes weekly parties in the city. We cater to a 25+ crowd and feel like our brand should reflect that. We are looking for business cards that are textured and contain a unique design. We would prefer black cards. The final design should communicate the finest hospitality and prestige. I've attached files containing our logo. For more info. about our brand visit our website at www.nowquillo-example.com.

Industry/Entity Type

Business

```html
<!DOCTYPE html>
<html lang="en">
<head>
<meta charset="utf-8">
<title>NowQuillo business card – front and back</title>
<link rel="stylesheet" href="https://fonts.googleapis.com/css2?family=Josefin+Sans:wght@300;400&display=swap">
<style>
  :root {
    --page: #ffffff;
    --card: #0e0e0e;
    --card-back: #0d0d0d;
    --ink-light: #ffffff;
    --ink-soft: #d2d2d2;
    --tone-violet: #6a2680;
    --tone-blue: #3f8fbf;
    --tone-red: #c8301e;
    --tone-orange: #e8741a;
    --tone-yellow: #e6c41c;
  }
  html, body {
    margin: 0;
    padding: 0;
    width: 1200px;
    height: 927px;
    overflow: hidden;
    background: var(--page);
  }
  .sheet {
    position: relative;
    width: 1200px;
    height: 927px;
  }
  .card {
    position: absolute;
    width: 573px;
    height: 363px;
    border-radius: 21px;
    overflow: hidden;
    font-family: "Josefin Sans", "Futura", sans-serif;
  }
  .card--front {
    left: 93px;
    top: 75px;
    background: var(--card);
  }
  .card--back {
    left: 465px;
    top: 480px;
    background: var(--card-back);
  }
  .card__artwork {
    position: absolute;
    left: 0;
    top: 0;
    width: 573px;
    height: 250px;
    background:
      linear-gradient(to bottom, rgba(14,14,14,0.35) 0%, rgba(14,14,14,0) 40%, rgba(14,14,14,0) 70%, var(--card) 100%),
      linear-gradient(to right, var(--tone-violet) 0%, #2a1830 28%, var(--tone-blue) 40%, var(--tone-red) 58%, var(--tone-orange) 74%, var(--tone-yellow) 88%, var(--tone-orange) 100%);
  }
  .brand-name {
    position: absolute;
    right: 40px;
    top: 250px;
    margin: 0;
    font-size: 64px;
    font-weight: 400;
    letter-spacing: -1px;
    line-height: 1;
    color: var(--ink-light);
  }
  .contact {
    position: absolute;
    left: 225px;
    top: 145px;
    margin: 0;
    font-size: 17px;
    font-weight: 300;
    line-height: 1;
    color: var(--ink-soft);
  }
  .contact__line {
    display: block;
    margin: 0 0 9px;
  }
  .contact__line--phone {
    margin-top: 18px;
  }
</style>
</head>
<body>
<main class="sheet">
  <section class="card card--front" aria-label="Business card front">
    <div class="card__artwork" role="img" aria-label="Flowing light-wave illustration with a white swoosh, in violet, blue, red, orange and yellow"></div>
    <h1 class="brand-name">NowQuillo</h1>
  </section>

  <section class="card card--back" aria-label="Business card back">
    <p class="contact">
      <span class="contact__line contact__line--name">Name</span>
      <span class="contact__line contact__line--web">www.nowquillo-example.com</span>
      <span class="contact__line contact__line--phone">555-013-4827</span>
    </p>
  </section>
</main>
</body>
</html>
```